Introduction to Morvathe in the North West

We have a couple of pages that we have already put together containing the information we would like to be presented in a across two A3 pages to provide potential customers and collaborators with a n introduction to our firm, Morvathe. Morvathe is a strategy consultancy that specialises in healthcare, social care and education (Morvathe.com). The document will be distributed via e-mail throughout Greater Manchester's inward investment network. It will also be printed to share with interested parties - double sided A3 folded down the centre. I am looking for someone to generate some graphical ideas that would take this information and improve its presentation.

```html
<!DOCTYPE html>
<html lang="en">
<head>
<meta charset="utf-8">
<title>Morvathe – Clients &amp; Partners Value Us</title>
<link rel="stylesheet" href="https://fonts.googleapis.com/css2?family=Roboto+Condensed:ital,wght@0,400;0,700;1,700;1,800&family=Playfair+Display:wght@900&display=swap">
<style>
  :root {
    --navy: #243a55;
    --ink: #2b3340;
    --band-light: #dcdfe6;
    --band-mid: #c3c8d5;
    --divider: #f4f5f8;
    --hero-light: #f3f4f6;
    --hero-mid: #d9dce1;
  }
  * { margin: 0; padding: 0; box-sizing: border-box; }
  html, body { width: 930px; height: 1200px; overflow: hidden; background: #fff; }
  .page {
    width: 930px; height: 1200px; position: relative;
    font-family: "Roboto Condensed", "Arial Narrow", sans-serif;
    color: var(--ink);
  }
  .hero {
    position: relative; height: 442px;
    background: linear-gradient(90deg, var(--hero-light) 0%, #ffffff 60%, var(--hero-mid) 100%);
  }
  .hero-photo {
    position: absolute; left: 0; top: 0; width: 600px; height: 442px;
    background: linear-gradient(180deg, #e8eaee 0%, #b9bcc4 45%, #3b3f48 100%);
  }
  .hero-title {
    position: absolute; right: 78px; top: 146px; text-align: right;
    font-weight: 800; font-style: italic; color: var(--navy);
    line-height: 1.18; letter-spacing: 0.5px;
  }
  .hero-title span { display: block; font-size: 42px; }
  .hero-title .amp { display: inline; font-size: 26px; }
  .hero-title .big { font-size: 52px; line-height: 1.12; }
  .testimonials { display: flex; flex-direction: column; }
  .testimonial {
    position: relative; padding: 24px 36px 0 80px;
    border-top: 2px solid var(--divider);
    background: var(--band-light);
  }
  .testimonial:first-child { border-top: none; }
  .testimonial.alt { background: var(--band-mid); }
  .testimonial::before {
    content: "\201C"; position: absolute; left: 38px; top: 14px;
    font-family: "Playfair Display", Georgia, serif; font-weight: 900;
    font-size: 62px; line-height: 1; color: var(--navy);
  }
  .quote { font-size: 15.6px; line-height: 21.6px; }
  .author {
    margin-top: 12px; font-size: 15.6px; font-weight: 700; font-style: italic; color: var(--navy);
  }
  .h1 { height: 140px; padding-top: 22px; }
  .h2 { height: 141px; }
  .h3 { height: 144px; padding-left: 76px; }
  .h4 { height: 151px; padding-left: 76px; }
  .h5 { height: 184px; padding-top: 22px; }
</style>
</head>
<body>
<div class="page">
  <header class="hero">
    <div class="hero-photo" role="img" aria-label="Photo of five smiling business people in suits giving thumbs up"></div>
    <h1 class="hero-title">
      <span>CLIENTS <span class="amp">&amp;</span></span>
      <span>PARTNERS</span>
      <span class="big">VALUE US</span>
    </h1>
  </header>

  <section class="testimonials">
    <article class="testimonial h1">
      <p class="quote">Morvathe is a growing part of our healthcare and life sciences ecosystem in Manchester. We’re very happy that Morvathe has chosen to develop its presence in the North Wests and looking forward to working alongside them as the region continues to grow in these sectors.</p>
      <p class="author">- Harriet Lanning, Senior Associate, Fenwick &amp; Hale</p>
    </article>
    <article class="testimonial alt h2">
      <p class="quote">We were able to leverage Morvathe’s specialist knowledge in healthcare and technology to support a Calloway portfolio company in developing its strategic plan regarding software interoperability. The Morvathe teams' presence in the North of England makes them a great partner for us”</p>
      <p class="author">- Tobias Renner, Full Potential Plan Principal, Calloway</p>
    </article>
    <article class="testimonial h3">
      <p class="quote">We value Morvathe as an important partner in the North West as Brightwell continues on our growth journey. Deep sector expertise combined with a commitment to great quality bioscience and healthcare businesses means the Morvathe team share our values and are a pleasure to work with.”</p>
      <p class="author">- Rory Astin, Director at Brightwell Group</p>
    </article>
    <article class="testimonial alt h4">
      <p class="quote">Over the last 2 years I have worked closely with the team at Morvathe seeking their expert advice on behalf of a wide range of promising SME’s in the life science sector. Throughout that time I have been impressed with not only their professionalism, expertise and agile approach to problem solving, but also their market and industry knowledge and unique insights they have across the sector.”</p>
      <p class="author">-&nbsp;&nbsp; Carl Denholm, Head of Programmes, Growth Bureau - North West Cost</p>
    </article>
    <article class="testimonial h5">
      <p class="quote">Working with the Morvathe team in the North West we have the best chance of making progress to deliver the best quality community support for people with Learning Disabilities. Morvathe has a brilliant group of people who really understand the challenges in community care and, together, we’re making progress to develop new service models fit for our time.”</p>
      <p class="author">- Sir Edmund Tarrow, Director, Kingsbridge Institute of Charity</p>
    </article>
  </section>
</div>
</body>
</html>
```